Create Website for new company called "Verdant Lodge 17"

Verdant Lodge 17 is a new business situated in Southwestern Colorado. We are creating a business that will rent out spaces where clients can grow their own marijuana. Picture a large green house with partitioned spaces that are secured by a lock. Best way to envision this would be to think of a storage business that rents out storage rooms. The difference is that we will be having the units inside a green house ( for growing purposes) Picture a small area that is secured by locks, Picture an area that has the ability to provide state of the art security, cameras etc. We want to focus our efforts on professionals, blue collar workers and end users of marijuana. Our emphasis is in the area of assisting those whom wish to grow their own plants. We want to provide them a safe facility in which to do that. . Keep in mind that we also build custom grow rooms at clients homes and provide a grow pod (lease these) where a small grow unit will be delivered and picked up from our clients whom want to lease a unit for a short amount of time. We have a business card ( just designed) and will send that information to those whom express an interests in this project. We want to be able to sign people up for our services by entering an agreement and signing the agreement while on the internet. We want to provide our services to those whom consume recreational and medical marijuana. This site will need to gather information I.e email addresses so that we can followup with offers. This is a tremendous opportunity for the right designer. We will be creating many more websites as other states come on line and make marijuana legal to consume. Use the business card model for a point of reference of how we envision the concept. That is a business card we just recently printed. The hands and the plant is our logo so far. Open to suggestions. There will be three levels of service. Bronze, Silver, Gold or Platinum. We will also have a retail biz down the road but not at the present time.

Target Market(s)

Ages 21-60

Industry/Entity Type

Medical

Logo Text

Verdant Lodge 17.

Number of Pages Required

5+ page

Requirements
Must have
• Clean appearance not to busy , easily navigable from link to link, page to page. Must have ability down the road to enter into a contractual agreement via the website. Must use our provided logo and example of that is on our business card that will be uploaded here shortly. We would like to have the colors that are on the business card however if you have suggestions or color schemes that you want us to consider that is okay.
Nice to have
• Nice to have a animation of seed to weed and how clients can save a tremendous amount of money growing their own cannabis. Nice to have testimonial page or feedback page. Have a membership component to website,
Should not have
• No flashing lights, etc. Not to busy in terms of animations.

```html
<!DOCTYPE html>
<html lang="en">
<head>
<meta charset="utf-8">
<title>Verdant Lodge 17</title>
<link rel="stylesheet" href="https://fonts.googleapis.com/css2?family=Oswald:wght@400;500&family=Lato:ital,wght@0,400;0,700;1,400&display=swap">
<style>
:root{
  --green:#0d8a3e;
  --green-dark:#06692c;
  --green-light:#1fa34f;
  --ink:#333;
  --muted:#6b6b6b;
  --panel:#f4f4f4;
  --grey-box:#666;
  --black:#000;
  --white:#fff;
  --line:#bdbdbd;
}
*{box-sizing:border-box;margin:0;padding:0}
html,body{width:780px;height:1200px;overflow:hidden}
body{position:relative;font-family:"Lato",sans-serif;color:var(--ink);background:var(--white)}
.abs{position:absolute}
.heading{font-family:"Oswald",sans-serif;font-weight:400}

/* header */
.topbar{left:0;top:0;width:780px;height:53px;background:linear-gradient(#0a9b45,var(--green-dark))}
.topbar .phone{left:86px;top:17px;color:var(--white);font-size:16px;display:flex;align-items:center;gap:6px}
.social{display:flex;gap:6px}
.social span{width:22px;height:22px;border-radius:50%;background:var(--white);display:block}
.topbar .social{left:590px;top:15px}
.nav{left:0;top:53px;width:780px;height:35px;background:var(--white)}
.nav a{position:absolute;top:0;height:35px;line-height:35px;font-family:"Oswald",sans-serif;font-size:10.5px;color:#333;text-decoration:none;text-align:center;letter-spacing:.3px}
.nav a.sep{border-right:1px solid #c9c9c9;height:22px;top:6px;line-height:22px}
.nav a.active{background:var(--green);color:var(--white);top:5px;height:25px;line-height:25px}
.brand{left:300px;top:5px;width:180px;height:100px;background:var(--white);border:5px solid #4fb070;display:flex;align-items:center;justify-content:center;gap:6px;box-shadow:0 2px 4px rgba(0,0,0,.2)}
.brand .mark{width:12px;height:12px;border-radius:50%;background:var(--green)}
.brand .name{font-family:"Oswald",sans-serif;font-size:20px;color:#333}

/* hero */
.hero{left:0;top:88px;width:780px;height:311px;background:radial-gradient(ellipse at 45% 45%,#7fae52 0%,#3f7a2e 40%,#1d3f17 100%)}
.arrow{width:30px;height:30px;border-radius:50%;border:2px solid #ddd;background:rgba(0,0,0,.35)}
.hero-caption{left:440px;top:270px;width:254px;height:66px;background:rgba(0,0,0,.55);color:var(--white);text-align:right;padding:4px 18px 0 0;font-size:20.5px;line-height:29px}

/* service cards */
.services{left:0;top:399px;width:780px;height:208px;background:var(--panel)}
.card{top:364px;width:188px;height:212px;background:var(--white);border:1px solid #aaa;border-radius:5px;overflow:hidden;box-shadow:0 8px 6px -6px rgba(0,0,0,.35)}
.card h3{height:36px;line-height:36px;padding-left:13px;font-size:15px;color:var(--white);background:linear-gradient(var(--green-light),var(--green-dark));font-weight:400}
.card .thumb{margin:10px 0 0 10px;width:168px;height:72px;border:3px solid #7a7a7a}
.card p{margin:9px 9px 0 10px;height:58px;overflow:hidden;font-size:9.2px;line-height:14.5px;color:var(--muted);letter-spacing:-.1px}
.more{display:block;margin:4px 10px 0;font-size:8px;font-weight:700;color:#333;text-decoration:underline}

/* welcome */
.welcome{left:0;top:607px;width:780px;height:183px;background:linear-gradient(#1a9a4a,var(--green-dark))}
.video{left:86px;top:625px;width:188px;height:147px;border-radius:5px;overflow:hidden;background:#cfcfcf}
.video .vname{position:absolute;left:0;top:80px;width:100%;text-align:center;font-family:"Oswald",sans-serif;font-size:19px;line-height:24px;color:#333}
.video .play{position:absolute;left:82px;top:40px;width:24px;height:24px;border-radius:50%;background:rgba(255,255,255,.9)}
.video .play::after{content:"";position:absolute;left:9px;top:6px;border-left:8px solid #333;border-top:6px solid transparent;border-bottom:6px solid transparent}
.video .controls{position:absolute;left:0;bottom:0;width:100%;height:20px;background:#111;color:#ddd;font-size:7px}
.welcome-text{left:297px;top:624px;width:398px;color:var(--white)}
.welcome-text h2{font-size:17.5px;font-weight:400;padding-bottom:6px;border-bottom:1px solid rgba(255,255,255,.7)}
.welcome-text p{font-size:9.1px;line-height:13px;margin-top:10px}
.welcome-text .more{color:var(--white);margin:4px 0 0}

/* testimonial / news */
.lower{left:0;top:790px;width:780px;height:225px;background:linear-gradient(#f4f4f4,#dedede)}
.sec-title{display:flex;align-items:center;gap:8px;font-size:14.5px;color:#333;padding-bottom:6px;border-bottom:1px solid #888}
.quote{left:86px;top:855px;width:280px;height:106px;background:var(--grey-box);border-radius:4px;color:var(--white);font-style:italic;font-size:8.9px;line-height:15px;padding:24px 12px 0 18px}
.quote::after{content:"";position:absolute;left:28px;bottom:-12px;border-right:18px solid transparent;border-top:12px solid var(--grey-box)}
.qmark{display:inline-block;height:10px;line-height:14px;font-family:"Oswald",sans-serif;font-style:normal;font-size:22px;color:#bbb;vertical-align:-4px;overflow:visible}
.client{left:141px;top:968px;font-size:9.5px;font-weight:700}
.divider{left:388px;top:830px;width:2px;height:150px;background:linear-gradient(transparent,#bbb,transparent)}
.news-item{font-size:8.5px;font-weight:700;display:flex;align-items:center;gap:5px}
.news-item::before{content:"";width:9px;height:8px;background:#e8e8e8;border:1px solid #ddd}

/* footer */
.footer{left:0;top:1015px;width:780px;height:185px;background:var(--black)}
.quote-form{left:86px;top:1018px;width:187px;height:182px;background:#545454;padding:10px 12px}
.quote-form h4{display:flex;align-items:center;gap:8px;color:var(--white);font-size:14.5px;font-weight:400;margin-bottom:10px}
.field{width:164px;height:21px;border:1px solid #999;background:#5e5e5e;color:#aaa;font-size:7px;padding:6px 8px;margin-bottom:5px}
.field.msg{height:42px}
.btn{background:var(--green);color:var(--white);font-size:10px;text-align:center}
.f-title{color:var(--white);font-size:12px}
.f-text{color:var(--white);font-size:8.5px;line-height:13px}
.vline{width:1px;background:#555}
.hline{height:1px;background:#555}
</style>
</head>
<body>

<header>
  <div class="abs topbar">
    <div class="abs phone">
      <svg width="18" height="18" viewBox="0 0 18 18"><circle cx="9" cy="9" r="8" fill="none" stroke="#fff" stroke-width="1.5"/><path d="M6 5l2 2-1 1.2c.6 1.3 1.5 2.2 2.8 2.8L11 10l2 2-1.3 1.5C8.5 13 5 9.5 4.5 6.3z" fill="#fff"/></svg>
      970-555-0172
    </div>
    <div class="abs social"><span></span><span></span><span></span><span></span></div>
  </div>
  <nav class="abs nav">
    <a class="active" style="left:86px;width:59px">HOME</a>
    <a class="sep" style="left:150px;width:75px">ABOUT US</a>
    <a style="left:235px;width:58px">SERVICES</a>
    <a class="sep" style="left:490px;width:57px">FACILITIES</a>
    <a class="sep" style="left:548px;width:73px">TESTIMONIAL</a>
    <a class="sep" style="left:622px;width:72px">CONTACT US</a>
  </nav>
  <div class="abs brand"><span class="mark"></span><span class="name">Verdant Lodge 17</span></div>
</header>

<section>
  <div class="abs hero" role="img" aria-label="Close-up photograph of young cannabis leaves growing"></div>
  <div class="abs arrow" style="left:55px;top:228px"><svg width="26" height="26"><path d="M15 8l-5 5 5 5" fill="none" stroke="#fff" stroke-width="2"/></svg></div>
  <div class="abs arrow" style="left:694px;top:228px"><svg width="26" height="26"><path d="M11 8l5 5-5 5" fill="none" stroke="#fff" stroke-width="2"/></svg></div>
  <div class="abs hero-caption heading">Supporting the care and the<br>Cultivation of Cannabis</div>
</section>

<section>
  <div class="abs services"></div>
  <article class="abs card" style="left:86px">
    <h3 class="heading">HELP U GROW</h3>
    <div class="thumb" role="img" aria-label="Hands holding soil with a seedling" style="background:linear-gradient(135deg,#8a8f99,#3a2a1c 55%,#6c8f3a)"></div>
    <p>We here at Verdant Lodge 17 have put together a variety of options that can help you grow your marijuana. We provide clients with various options...</p>
    <a class="more">READ MORE »</a>
  </article>
  <article class="abs card" style="left:297px">
    <h3 class="heading">SECURITY</h3>
    <div class="thumb" role="img" aria-label="Security camera mounted on a brick wall" style="background:linear-gradient(90deg,#4f7fd0,#6d9be0 60%,#a0583c 75%)"></div>
    <p>Lorem ipsum dolor sit ametuer adipiscingi elit, sed diam nmy nibh euismod tincidunt ut laoreet dolore magna am erat visi enim ad minim veniam, quis nostrud...</p>
    <a class="more">READ MORE »</a>
  </article>
  <article class="abs card" style="left:508px">
    <h3 class="heading">ONLINE ACCESS</h3>
    <div class="thumb" role="img" aria-label="Screen showing the online camera portal" style="background:linear-gradient(90deg,#222 0 12%,#f2f2f2 12%)"></div>
    <p>Online access to the security cameras are needed for security reasons. Both the exterior and interior common areas will have security cameras that will be...</p>
    <a class="more">READ MORE »</a>
  </article>
</section>

<section>
  <div class="abs welcome"></div>
  <div class="abs video" role="img" aria-label="Introductory video player">
    <span class="play"></span>
    <div class="vname">Verdant Lodge 17</div>
    <div class="controls">
      <svg width="188" height="20" viewBox="0 0 188 20">
        <path d="M8 6v8l6-4z" fill="#ddd"/>
        <text x="28" y="13" fill="#ddd" font-size="7" font-family="Lato,sans-serif">04:59</text>
        <rect x="52" y="8" width="70" height="4" rx="2" fill="#555"/><rect x="52" y="8" width="50" height="4" rx="2" fill="#888"/>
        <text x="126" y="13" fill="#ddd" font-size="7" font-family="Lato,sans-serif">10:35</text>
        <path d="M152 8h2l3-3v10l-3-3h-2z" fill="#ddd"/>
        <path d="M172 6l8 8M172 6v3M172 6h3M180 14v-3M180 14h-3" stroke="#ddd" stroke-width="1.3"/>
      </svg>
    </div>
  </div>
  <div class="abs welcome-text">
    <h2 class="heading">Welcome To Verdant Lodge 17</h2>
    <p>Colorado residents voted to make the recreational consumption of Cannabis legal. Now that its legally permissible to grow your own marijuana we here at Verdant Lodge 17 are here to help. We offer the following: grow spaces, grow pods, customized grow rooms, custom built grow rooms. In addition to the aforementioned we also offer our expertise in various areas such as nutrition, logistics, automation controls, etc.</p>
    <p style="margin-top:6px">We are not a marijuana establishment however we are support the care and the cultivation of those Colorado residents whom wish to grow their own marijuana.</p>
    <a class="more">READ MORE »</a>
  </div>
</section>

<section>
  <div class="abs lower"></div>
  <div class="abs" style="left:86px;top:810px;width:281px">
    <div class="sec-title heading">
      <svg width="20" height="18" viewBox="0 0 20 18"><path d="M1 1h12v8H6l-3 3V9H1z" fill="#0d8a3e"/><path d="M8 10h5l1-1V5h5v8h-2v3l-3-3H8z" fill="#0d8a3e"/></svg>
      Client Testimonial
    </div>
  </div>
  <blockquote class="abs quote"><span class="qmark">“</span>&nbsp; I cannot drive and Verdant Lodge 17 provided me the option of leasing a grow pod. The grow pod had all the automation controls already in it. They helped me by referring me to a local cannabis source where I bought my plants <span class="qmark">”</span></blockquote>
  <div class="abs client">Marla Trent</div>
  <div class="abs divider"></div>
  <div class="abs" style="left:414px;top:810px;width:281px">
    <div class="sec-title heading">
      <svg width="20" height="18" viewBox="0 0 20 18"><path d="M1 6h4l10-5v15L5 11H1z" fill="#0d8a3e"/><path d="M5 11l2 6h3l-2-6z" fill="#0d8a3e"/></svg>
      Latest News
    </div>
  </div>
  <div class="abs news-item" style="left:414px;top:853px">To Be Updated Soon</div>
  <div class="abs" style="left:414px;top:916px;width:281px;border-top:1px dotted #888"></div>
  <div class="abs news-item" style="left:414px;top:929px">To Be Updated Soon</div>
</section>

<footer>
  <div class="abs footer"></div>
  <form class="abs quote-form">
    <h4 class="heading">
      <svg width="20" height="16" viewBox="0 0 20 16"><path d="M1 6l9-5 9 5v9H1z" fill="none" stroke="#fff" stroke-width="1.5"/><path d="M1 6l9 6 9-6" fill="none" stroke="#fff" stroke-width="1.5"/></svg>
      Request a Quote
    </h4>
    <div class="field">Name</div>
    <div class="field">Email</div>
    <div class="field msg">Message</div>
    <div class="btn" style="width:48px;height:24px;line-height:24px;margin-top:3px">SEND</div>
  </form>

  <div class="abs f-title heading" style="left:297px;top:1028px">News Letter Signup</div>
  <div class="abs" style="left:296px;top:1051px;width:185px;height:24px;background:#6a6a6a;color:#eee;font-size:7.5px;line-height:24px;padding-left:8px">Enter Your Email</div>
  <div class="abs btn" style="left:486px;top:1051px;width:55px;height:24px;line-height:24px">SUBMIT</div>
  <div class="abs vline" style="left:569px;top:1036px;height:46px"></div>
  <div class="abs f-title heading" style="left:590px;top:1028px">Social Contact</div>
  <div class="abs social" style="left:590px;top:1053px"><span></span><span></span><span></span><span></span></div>
  <div class="abs hline" style="left:296px;top:1092px;width:399px"></div>

  <svg class="abs" style="left:296px;top:1108px" width="10" height="14" viewBox="0 0 10 14"><path d="M5 0a5 5 0 0 1 5 5c0 4-5 9-5 9S0 9 0 5a5 5 0 0 1 5-5z" fill="#fff"/><circle cx="5" cy="5" r="2" fill="#000"/></svg>
  <div class="abs f-text" style="left:314px;top:1106px;width:90px">Lorem ipsum dolor sit amet, consectetuer adipiscing eli sed di nonmmy</div>
  <svg class="abs" style="left:416px;top:1108px" width="8" height="11" viewBox="0 0 8 11"><rect x=".5" y=".5" width="7" height="10" rx="1.5" fill="none" stroke="#fff"/><rect x="2" y="2" width="4" height="5" fill="#fff"/></svg>
  <div class="abs f-text" style="left:432px;top:1107px;font-size:9px">970-555-0172</div>
  <svg class="abs" style="left:415px;top:1130px" width="10" height="8" viewBox="0 0 10 8"><rect x=".5" y=".5" width="9" height="7" fill="none" stroke="#fff"/><path d="M.5 .5l4.5 4 4.5-4" fill="none" stroke="#fff"/></svg>
  <div class="abs f-text" style="left:432px;top:1127px;font-size:8.5px">hello@verdantlodge17.com</div>
  <div class="abs f-text" style="left:414px;top:1147px;font-size:6.5px">Please call or email us for more information</div>
  <div class="abs vline" style="left:569px;top:1102px;height:56px"></div>
  <div class="abs" style="left:588px;top:1116px;display:flex;align-items:center;gap:5px">
    <span style="width:9px;height:9px;border-radius:50%;background:var(--green);display:block"></span>
    <span class="heading" style="color:var(--white);font-size:14px">Verdant Lodge 17</span>
  </div>
  <div class="abs hline" style="left:296px;top:1163px;width:399px"></div>
  <div class="abs f-text" style="left:305px;top:1176px;font-size:8.5px">© 2015 Verdant Lodge &nbsp;|&nbsp; All Rights Reserved</div>
</footer>

</body>
</html>
```